Business card - house cleaning company

We want friendly high end business card highlighting our services . NO LOGOs on back of card please.. no vertical cards NO DOUBLE BROOMS

2 owners of the company: Corinne Halvey & Joel Brandt

Included phone number: (555)318-2047

Email: brightlanetidy@mailnest.example

Website: www.brightlanetidy.example

Bonded & Insured

Estes Park, CO 80517

Slogan maybe: Bringing a brighter shine to every corner of home

We want elegant high end card for house cleaning service. Maybe 2 sided if needed. Can it have bullet points of some services we offer

Residential Home Cleaning
Vacation Rental Cleaning
Commercial Cleaning
Carpet Cleaning
Window Cleaning
Property Management
Property Inspections
Property Maintenance
Trash Removal
Concierge Services

Highlight service on back of card. If we can do a one sided card with all this that’s great as well. Not cartoony.

Our logo attached and a design somone I had Perrin but they put very little time in. Not Unique enough. If you can do a custom design with a feminine touch that be great.

You will be eliminated for not reading the brief. NO DOUBLE LOGOS NO DOUBLE BROOMS. PLEASE BE CREATIVE. IF POST SAME LOGO WITH SMAL CHANGES RHEY WILL BE ELIMINATED. BE CREATIVE.

Thank you everyone for your designs. please only use the logo 1 time. and would love to see some that dont look all the same. We appreciate your time.

Target Market(s)

Residential and vacation rental home cleaning maid service

Industry/Entity Type

House cleaning maid services

Contact Information for Business Card

For business card use logo. black and green one provided. others for example. I wil try find some example.. We want friendly high end look. 2 owners of the company: Corinne Halvey & Joel Brandt Included phone number: (555)318-2047 Email: brightlanetidy@mailnest.example Website: www.brightlanetidy.example Bonded & Insured Estes Park, CO Slogan maybe: Bringing a brighter shine to every corner of home or Quality Service Guaranteed We want elegant high end card for house cleaning service. Maybe 2 sided if needed. Can it have bullet points of some services we offer Residential Home Cleaning Vacation Rental Cleaning Commercial Cleaning Carpet Cleaning Window Cleaning Property Management Property Inspections Property Maintenance Trash Removal Concierge Services

Requirements
Must have
• For business card use logo . Creativity. black and green one provided. We want friendly high end look. 2 owners of the company: Corinne Halvey & Joel Brandt Included phone number: (555)318-2047 Email: brightlanetidy@mailnest.example Website: www.brightlanetidy.example Licensed Bonded & Insured Estes Park, CO Slogan maybe: Bringing a brighter shine to every corner of home or Quality Service Guaranteed We want elegant high end card for house cleaning service. Maybe 2 sided if needed. Can it have bullet points of some services we offer Residential Home Cleaning Vacation Rental Cleaning Commercial Cleaning Carpet Cleaning Window Cleaning Property Management Property Inspections Property Maintenance Trash Removal Concierge Services .. creatitivty a plus. whimsical. we like stars..
Nice to have
• we want much better than the example of biz card provided as example. logo has colors that are in our website palette as well. We are open to ideas for the business card design. Will pay tip to best work. PLEASE USE COMPLIMENTING COLORS. . WE LIKE BLACK AND WHITE, stars
Should not have
• NO DOUBLE LOGOS. READ READ. READ. YOU WILL BE ELIMINATED no double logos or double brooms same side of card. I want didfrent examples. please don't make all your submission look the same

```html
<!DOCTYPE html>
<html lang="en">
<head>
<meta charset="utf-8">
<title>Bright Lane Tidy – Business Card</title>
<link rel="stylesheet" href="https://fonts.googleapis.com/css2?family=EB+Garamond:wght@400;500&family=Dancing+Script:wght@500&display=swap">
<style>
  :root {
    --ink-green: #3b4a22;
    --ink-dark: #26261f;
    --logo-panel: #e2e8d2;
    --side-band: #bccaa3;
    --veil: rgba(255, 253, 246, 0.74);
    --room-top: #f7f2e8;
    --room-mid: #efe6d6;
    --room-low: #d6e5e3;
  }
  * { margin: 0; padding: 0; box-sizing: border-box; }
  html, body { width: 1200px; height: 732px; overflow: hidden; background: #ffffff; }
  .card {
    position: relative;
    width: 1200px;
    height: 732px;
    overflow: hidden;
    font-family: "EB Garamond", Georgia, serif;
    color: var(--ink-green);
  }
  .room-backdrop {
    position: absolute; inset: 0;
    background:
      radial-gradient(ellipse 420px 160px at 600px 560px, rgba(232, 196, 170, 0.5), transparent 70%),
      radial-gradient(ellipse 260px 140px at 260px 520px, rgba(236, 200, 186, 0.45), transparent 70%),
      linear-gradient(180deg, var(--room-top) 0%, var(--room-mid) 55%, var(--room-low) 100%);
  }
  .light-veil {
    position: absolute; left: 0; top: 0; width: 556px; height: 732px;
    background: linear-gradient(90deg, var(--veil) 0%, rgba(255,253,246,0.55) 100%);
  }
  .side-band {
    position: absolute; left: 1166px; top: 40px; width: 34px; height: 602px;
    background: var(--side-band); opacity: 0.8;
  }
  .service-list { list-style: none; }
  .service-list li {
    position: absolute; left: 31px;
    font-size: 42px; line-height: 50px; height: 50px;
    white-space: nowrap; color: var(--ink-green);
  }
  .brand-panel {
    position: absolute; left: 556px; top: 40px; width: 610px; height: 270px;
    background: var(--logo-panel);
    display: flex; align-items: center; justify-content: center;
  }
  .brand-name {
    font-size: 80px; font-weight: 500; color: var(--ink-dark);
    white-space: nowrap;
  }
  .contact { font-style: normal; color: var(--ink-dark); }
  .contact p {
    position: absolute; right: 45px;
    text-align: right; white-space: nowrap;
  }
  .contact .owners { font-size: 43px; line-height: 46px; top: 368px; }
  .contact .phone { font-size: 40px; line-height: 44px; top: 411px; }
  .contact .line { font-size: 30px; line-height: 36px; }
  .slogan {
    position: absolute; left: 184px; top: 636px;
    font-family: "Dancing Script", cursive;
    font-size: 54px; line-height: 66px; color: var(--ink-dark);
    white-space: nowrap;
  }
</style>
</head>
<body>
  <main class="card">
    <div class="room-backdrop" role="img" aria-label="Softly lit living room with a pale sofa and pastel striped cushions"></div>
    <div class="light-veil"></div>
    <div class="side-band"></div>

    <ul class="service-list">
      <li style="top: 29px;">Residential Home Cleaning</li>
      <li style="top: 90px;">Vacation Rental Cleaning</li>
      <li style="top: 150px;">Commercial Cleaning</li>
      <li style="top: 210px;">Carpet Cleaning</li>
      <li style="top: 271px;">Window Cleaning</li>
      <li style="top: 331px;">Property Management</li>
      <li style="top: 391px;">Property Inspections</li>
      <li style="top: 451px;">Property Maintenance</li>
      <li style="top: 517px;">Trash Removal</li>
      <li style="top: 572px;">Concierge Services</li>
    </ul>

    <div class="brand-panel">
      <span class="brand-name">Bright Lane Tidy</span>
    </div>

    <address class="contact">
      <p class="owners">Corinne Halvey &amp; Joel Brandt</p>
      <p class="phone">Phone: (555)318-2047</p>
      <p class="line" style="top: 456px;">Email: brightlanetidy@mailnest.example</p>
      <p class="line" style="top: 500px;">Website: www.brightlanetidy.example</p>
      <p class="line" style="top: 537px;">Bonded &amp; Insured</p>
      <p class="line" style="top: 577px;">Estes Park, CO 80517</p>
    </address>

    <p class="slogan">Bringing a brighter shine to every corner of home</p>
  </main>
</body>
</html>
```